Corporate Design für Emotionscoach
Vielen Dank für die sehr gute, kreative und schnelle Zusammenarbeit. Thank you very much for the very good, creative and fast cooperation
Zielgruppe
Ich bin Emotionscoach und Experte für Emotionale Intelligenz
Mein Angebot richtet sich vorwiegend an Geschäftsleute (mittelständische Unternehmer, Führungskräfte, Vertriebskräfte), deren Mitarbeiter und auch Privatpersonen.
In meinen Coachings und Seminaren lernen die Menschen ihre eigenen Emotionen und die ihrer Gesprächspartner, in den verschiedensten Lebensbereichen wahrnehmen, verstehen und gezielt zu beeinflussen. Sowohl in geschäftlichen (z.B. Führung, Teamentwicklung, Vertrieb) als auch im privaten Bereich, hilft der bewusste Umgang mit Emotionen, um Veränderungen und Wachstum zu ermöglichen sowie individuelle (Gesprächs-) Ziele besser, leichter zu erreichen und damit erfolgreicher zu sein.
Weitere Informationen finden sie auh auf meiner Homepage (www.lumen-wegweiser.de)
Aufgabenstellung
Die farbliche Gestaltung meines Designgs möchte ich gerne an den Farben meiner Homepage (Farbcodes: #90c80d bzw. #8cc902) orientieren.
Es soll für Wete wie persönliche Weiterentwicklung, Veränderungsbereitschaft und Neugier stehen

```html
<!DOCTYPE html>
<html lang="de">
<head>
<meta charset="utf-8">
<title>Coaching Halden – Corporate Design</title>
<link rel="stylesheet" href="https://fonts.googleapis.com/css2?family=Montserrat:wght@400;500;600&display=swap">
<style>
  :root{
    --green:#8cc63f;
    --ink:#2b2b2b;
    --paper:#ffffff;
    --stage:#f7f7f7;
    --window:#cfcfcf;
    --ghost:#f1f1f2;
    --shadow:0 2px 6px rgba(0,0,0,.22);
  }
  *{box-sizing:border-box;margin:0;padding:0}
  html,body{width:1200px;height:1200px;overflow:hidden;background:#fff}
  body{position:relative;font-family:"Montserrat",sans-serif;color:var(--ink)}
  .stage{position:absolute;left:184px;top:0;width:838px;height:1200px;background:var(--stage)}
  .tile,.card,.envelope,.letter{position:absolute;background:var(--paper)}
  .tile{display:flex;align-items:center;justify-content:center}
  .tile--green{background:var(--green)}
  .card,.envelope,.letter{box-shadow:var(--shadow)}
  .label{position:absolute;font-size:8px;color:var(--ink)}

  /* brand lockup */
  .lockup{display:flex;align-items:center;gap:calc(var(--s)*7px)}
  .lockup--v{flex-direction:column;gap:calc(var(--s)*6px)}
  .lockup--abs{position:absolute}
  .lockup__dot{width:calc(var(--s)*30px);height:calc(var(--s)*30px);border-radius:50%;background:var(--green);flex:none}
  .lockup__text{display:flex;flex-direction:column;align-items:center}
  .lockup__name{font-family:"Montserrat",sans-serif;font-weight:500;font-size:calc(var(--s)*15px);line-height:1.1;color:var(--green);white-space:nowrap}
  .lockup__tag{font-size:calc(var(--s)*4.6px);letter-spacing:.12em;margin-top:calc(var(--s)*4px);white-space:nowrap;color:var(--ink)}
  .on-green .lockup__dot{background:#fff}
  .on-green .lockup__name{color:#fff}
  .on-green .lockup__tag{color:#fff}
  .on-green.alt .lockup__name{color:var(--ink)}

  .card__stripe{position:absolute;left:3px;top:3px;bottom:3px;width:4px;background:var(--green)}
  .card__mark{position:absolute;left:22px;top:8px;width:28px;height:28px;border-radius:50%;background:var(--green)}
  .card__contact{position:absolute;right:8px;top:40px;text-align:right;font-size:3.6px;line-height:1.4}
  .card__contact strong{display:block;font-size:5.4px;margin-bottom:5px}
  .card__contact .gap{display:block;height:3px}

  .envelope__window{position:absolute;left:34px;top:80px;width:162px;height:70px;border-radius:4px;background:var(--window)}
  .flap{position:absolute;left:0;top:0}
  .flap__mark{position:absolute;left:164px;top:12px;width:32px;height:32px;border-radius:50%;background:#fff}
  .envelope__url{position:absolute;left:0;right:0;bottom:8px;text-align:center;font-size:5px;font-weight:600}

  .letter__sender{position:absolute;left:23px;top:99px;font-size:4.6px}
  .letter__fold{position:absolute;left:0;width:8px;height:1px;background:#999}
  .letter__footer{position:absolute;left:54px;bottom:10px;display:flex;font-size:4.4px;line-height:1.3}
  .letter__footer div{padding:0 9px;border-left:.6px solid var(--ink)}
  .letter__footer div:first-child{border:0;padding-left:0}
  .letter__band{position:absolute;left:42px;bottom:0;width:257px;height:4px;background:var(--green)}
</style>
</head>
<body>
<div class="stage"></div>

<!-- logo variants -->
<section class="tile" style="left:273px;top:24px;width:208px;height:148px">
  <div class="lockup" style="--s:1"><span class="lockup__dot"></span><div class="lockup__text"><span class="lockup__name">Coaching Halden</span><span class="lockup__tag">Begleitung für Wandel und Wachstum</span></div></div>
</section>
<section class="tile tile--green on-green" style="left:485px;top:24px;width:207px;height:148px">
  <div class="lockup" style="--s:1"><span class="lockup__dot"></span><div class="lockup__text"><span class="lockup__name">Coaching Halden</span><span class="lockup__tag">Begleitung für Wandel und Wachstum</span></div></div>
</section>
<section class="tile tile--green on-green alt" style="left:699px;top:24px;width:207px;height:148px">
  <div class="lockup" style="--s:1"><span class="lockup__dot"></span><div class="lockup__text"><span class="lockup__name">Coaching Halden</span><span class="lockup__tag">Begleitung für Wandel und Wachstum</span></div></div>
</section>
<section class="tile" style="left:273px;top:180px;width:208px;height:148px">
  <div class="lockup lockup--v" style="--s:1.15"><span class="lockup__dot"></span><div class="lockup__text"><span class="lockup__name">Coaching Halden</span><span class="lockup__tag">Begleitung für Wandel und Wachstum</span></div></div>
</section>
<section class="tile tile--green on-green" style="left:485px;top:180px;width:207px;height:148px">
  <div class="lockup lockup--v" style="--s:1.15"><span class="lockup__dot"></span><div class="lockup__text"><span class="lockup__name">Coaching Halden</span><span class="lockup__tag">Begleitung für Wandel und Wachstum</span></div></div>
</section>
<section class="tile tile--green on-green alt" style="left:699px;top:180px;width:207px;height:148px">
  <div class="lockup lockup--v" style="--s:1.15"><span class="lockup__dot"></span><div class="lockup__text"><span class="lockup__name">Coaching Halden</span><span class="lockup__tag">Begleitung für Wandel und Wachstum</span></div></div>
</section>

<!-- business cards -->
<span class="label" style="left:413px;top:369px">1</span>
<section class="card" style="left:434px;top:372px;width:140px;height:91px">
  <div class="lockup lockup--v lockup--abs" style="--s:.8;left:0;right:0;top:14px"><span class="lockup__dot"></span><div class="lockup__text"><span class="lockup__name">Coaching Halden</span><span class="lockup__tag">Begleitung für Wandel und Wachstum</span></div></div>
</section>
<span class="label" style="left:613px;top:369px">B</span>
<section class="card" style="left:624px;top:372px;width:140px;height:91px">
  <span class="card__stripe"></span>
  <span class="card__mark"></span>
  <div class="card__contact">
    <strong>Fritz Halden</strong>
    Am Wiesengrund 4<br>41460 Neuss am Rhein<span class="gap"></span>
    Tel. 02131 5550123<br>Mobil 01515 5550188<span class="gap"></span>
    fritz.halden@lumen-wegweiser.de<br><b>www.lumen-wegweiser.de</b>
  </div>
</section>

<!-- window envelope -->
<section class="envelope" style="left:226px;top:496px;width:358px;height:180px">
  <div class="lockup lockup--v lockup--abs" style="--s:.6;left:14px;top:8px"><span class="lockup__dot"></span><div class="lockup__text"><span class="lockup__name">Coaching Halden</span><span class="lockup__tag">Begleitung für Wandel und Wachstum</span></div></div>
  <span class="envelope__window"></span>
  <svg style="position:absolute;left:208px;top:50px" width="94" height="94" viewBox="0 0 94 94" role="img" aria-label="Brand symbol area"><circle cx="47" cy="47" r="46" fill="var(--green)"/></svg>
</section>

<!-- flap envelope -->
<section class="envelope" style="left:617px;top:497px;width:358px;height:180px">
  <svg class="flap" width="358" height="62" viewBox="0 0 358 62"><path d="M0 0H358L348 52Q346 61 337 61H21Q12 61 10 52Z" fill="var(--green)"/></svg>
  <span class="flap__mark"></span>
  <span class="envelope__url">www.lumen-wegweiser.de</span>
</section>

<!-- letterhead -->
<span class="label" style="left:400px;top:701px">2</span>
<section class="letter" style="left:420px;top:696px;width:342px;height:483px">
  <div class="lockup lockup--abs" style="--s:.92;right:14px;top:12px"><span class="lockup__dot"></span><div class="lockup__text"><span class="lockup__name">Coaching Halden</span><span class="lockup__tag">Begleitung für Wandel und Wachstum</span></div></div>
  <p class="letter__sender">Fritz Halden | Am Wiesengrund 4 | 41460 Neuss am Rhein</p>
  <span class="letter__fold" style="top:170px"></span>
  <span class="letter__fold" style="top:241px"></span>
  <span class="letter__fold" style="top:339px"></span>
  <svg style="position:absolute;left:84px;top:156px" width="160" height="160" viewBox="0 0 160 160" role="img" aria-label="Faint brand symbol watermark area"><circle cx="80" cy="80" r="78" fill="var(--ghost)"/></svg>
  <div class="letter__footer">
    <div>Am Wiesengrund 4<br>41460 Neuss am Rhein</div>
    <div>Tel. &nbsp;&nbsp;&nbsp;02131 5550123<br>Mobil 01515 5550188</div>
    <div>fritz.halden@lumen-wegweiser.de<br>www.lumen-wegweiser.de</div>
  </div>
  <span class="letter__band"></span>
</section>
</body>
</html>
```